Paint Protection Options

This is a flyer that will describe two different paint protection options for vehicles. I have mocked up a Word doc. As well, I've included some samples of other flyers where I like the "look". I am not locked into any single layout or design. In my Word doc I have them side-by-side. I think that makes sense but open to ideas. I've also added some pics of the two options being applied to cars. We need to have one of each (ceramic and ppf) at a minimum. In the grid I'm thinking different colors dots/circles to differentiate the different levels. But again, I'm open to suggestions. You can use the symbol for microns in the grid under the Thickness row. I spelled it out because I didn't know how to insert.

```html
<!DOCTYPE html>
<html lang="en">
<head>
<meta charset="utf-8">
<title>Paint Protection Options</title>
<link href="https://fonts.googleapis.com/css2?family=Montserrat:ital,wght@0,400;0,500;0,700;1,300;1,400;1,800;1,900&display=swap" rel="stylesheet">
<style>
  :root {
    --red: #c00000;
    --red-deep: #7a0000;
    --black: #000000;
    --ink: #111111;
    --white: #ffffff;
    --green: #12c82a;
    --yellow: #f7d417;
    --orange: #f7801e;
    --dot-red: #e0201e;
  }
  * { margin: 0; padding: 0; box-sizing: border-box; }
  html, body { width: 856px; height: 1200px; overflow: hidden; background: var(--white); }
  body { font-family: "Montserrat", Arial, sans-serif; color: var(--ink); }
  .flyer { position: relative; width: 856px; height: 1200px; overflow: hidden; }

  .hero { position: absolute; left: 0; top: 0; width: 856px; height: 390px; display: block; }

  .title { position: absolute; left: 53px; top: 98px; color: var(--white); font-style: italic; line-height: 0.93; }
  .title .strong { display: block; font-weight: 900; font-size: 58px; letter-spacing: 0.5px; }
  .title .light { display: block; font-weight: 300; font-size: 58px; letter-spacing: 1px; }

  .tab { position: absolute; color: var(--white); font-style: italic; }
  .tab .tab-name { display: block; font-weight: 900; font-size: 29px; line-height: 1; }
  .tab .tab-sub { display: block; font-weight: 400; font-size: 14px; letter-spacing: 0.3px; margin-top: 8px; }
  .tab-ppf { left: 52px; top: 333px; }
  .tab-ceramic { right: 56px; top: 552px; text-align: right; }

  .copy { position: absolute; font-size: 12.4px; line-height: 15.5px; font-weight: 500; }
  .copy p + p { margin-top: 15.5px; }
  .copy-ppf { left: 54px; top: 402px; width: 752px; }
  .copy-ceramic { left: 56px; top: 621px; width: 746px; text-align: right; }

  .bullets { position: absolute; list-style: none; font-size: 12.4px; line-height: 15.5px; font-weight: 500; }
  .bullets li { position: relative; }
  .bullets-left { left: 54px; top: 525px; }
  .bullets-left li { padding-left: 18px; }
  .bullets-left li::before { content: ""; position: absolute; left: 1px; top: 7px; width: 5px; height: 5px; border-radius: 50%; background: var(--ink); }
  .bullets-right { right: 54px; top: 759px; text-align: right; }
  .bullets-right li { padding-right: 13px; }
  .bullets-right li::after { content: ""; position: absolute; right: 0; top: 7px; width: 5px; height: 5px; border-radius: 50%; background: var(--ink); }

  .compare { position: absolute; left: 53px; top: 832px; width: 760px; border-collapse: collapse; font-size: 12.4px; font-weight: 500; }
  .compare th { font-weight: 700; font-size: 15px; letter-spacing: 0.4px; height: 24px; text-align: center; vertical-align: middle; padding-bottom: 4px; }
  .compare th.feature { text-align: left; }
  .compare td { height: 28px; text-align: center; vertical-align: middle; }
  .compare td.feature { text-align: left; }
  .compare .c-feature { width: 200px; }
  .compare .c-wax { width: 118px; }
  .compare .c-ceramic { width: 302px; }
  .compare .c-ppf { width: 140px; }
  .rating { width: 24px; height: 24px; display: inline-block; vertical-align: middle; }
</style>
</head>
<body>
<div class="flyer">

  <svg class="hero" viewBox="0 0 856 390" aria-hidden="false">
    <defs>
      <linearGradient id="shopPhoto" x1="0" y1="0" x2="1" y2="0.6">
        <stop offset="0" stop-color="#2a0a08"/>
        <stop offset="0.35" stop-color="#8e0b0b"/>
        <stop offset="0.7" stop-color="#d8141a"/>
        <stop offset="1" stop-color="#9b0808"/>
      </linearGradient>
      <linearGradient id="headlightPhoto" x1="0" y1="0" x2="0.4" y2="1">
        <stop offset="0" stop-color="#8fb4b8"/>
        <stop offset="0.45" stop-color="#3b5256"/>
        <stop offset="1" stop-color="#0d1214"/>
      </linearGradient>
      <linearGradient id="titleShade" x1="0" y1="0" x2="1" y2="0">
        <stop offset="0" stop-color="#1a0000" stop-opacity="0.85"/>
        <stop offset="1" stop-color="#a00000" stop-opacity="0.55"/>
      </linearGradient>
    </defs>
    <polygon role="img" aria-label="Photo: technician in gloves fitting protection film on a glossy red car"
             points="0,0 856,0 856,353 411,353 435,303 0,303" fill="url(#shopPhoto)"/>
    <polygon points="0,53 622,53 502,303 0,303" fill="url(#titleShade)"/>
    <polygon points="782,0 856,0 856,125 722,125" fill="#7a0000" opacity="0.55"/>
    <polygon role="img" aria-label="Photo: water beading on a coated car headlight"
             points="532,125 770,125 664,353 411,353" fill="url(#headlightPhoto)"/>
    <polygon points="0,323 276,323 244,390 0,390" fill="var(--black)"/>
    <polygon points="659,353 856,353 856,387 646,387" fill="var(--red)"/>
  </svg>

  <h1 class="title">
    <span class="strong">PAINT</span>
    <span class="strong">PROTECTION</span>
    <span class="light">OPTIONS</span>
  </h1>

  <div class="tab tab-ppf">
    <span class="tab-name">PPF</span>
    <span class="tab-sub">PAINT PROTECTION FILM</span>
  </div>

  <div class="copy copy-ppf">
    <p>Paint Protection Film (PPF) is a transparent, thermoplastic urethane film that is applied directly to the car’s painted surfaces. PPF excels at shielding your vehicle from rock chips, scratches, and other physical damage. It has self-healing properties that can repair minor scratches and swirl marks over time.</p>
    <p>Every piece of PPF is custom cut to fit each panel of your vehicle and provide maximum coverage. The film protects your vehicle from scratches, rock chips, staining, corrosion, fading, chemicals, insects, and road debris. It helps keep your paint looking new, saving you money and improving your resale value.</p>
  </div>

  <ul class="bullets bullets-left">
    <li>Protect against rock chips, scratches, and physical damage</li>
    <li>Easily repair minor scratches and swirl marks</li>
    <li>Protect against corrosion and contaminants</li>
  </ul>

  <svg style="position:absolute;left:0;top:0" width="856" height="620" aria-hidden="true">
    <polygon points="611,543 856,543 856,611 580,611" fill="var(--red)"/>
  </svg>

  <div class="tab tab-ceramic">
    <span class="tab-name">CERAMIC</span>
    <span class="tab-sub">COATINGS</span>
  </div>

  <div class="copy copy-ceramic">
    <p>Ceramic coatings are liquid polymer coatings that bond to a vehicle’s painted surface. The coatings are formulated to retain the showroom finish by protecting against corrosion and contaminants like UV damage, oxidation, road salt and acid rain.&nbsp; Ceramic coatings give your car a deep, glossy finish that reflects light and makes your paint look more vibrant while greatly extending the paint's lifespan.</p>
    <p>The chemical bonding process improves color depth and leaves a smooth finish. The hydrophobic (water repellent) properties repel water and dirt as well as protect against damaging pollutants.&nbsp; This makes care and maintenance a breeze while retaining the show room finish.&nbsp; Never wax again!</p>
  </div>

  <ul class="bullets bullets-right">
    <li>Enhance and retain showroom finish</li>
    <li>Protect against corrosion and contaminants</li>
    <li>Reduce care and maintenance</li>
  </ul>

  <svg width="0" height="0" style="position:absolute" aria-hidden="true">
    <defs>
      <symbol id="rate-full" viewBox="0 0 24 24">
        <circle cx="12" cy="12" r="10" fill="none" stroke="var(--green)" stroke-width="2.4"/>
        <circle cx="12" cy="12" r="7" fill="var(--green)"/>
      </symbol>
      <symbol id="rate-most" viewBox="0 0 24 24">
        <circle cx="12" cy="12" r="10" fill="none" stroke="var(--green)" stroke-width="2.4" stroke-dasharray="47 16" transform="rotate(-60 12 12)"/>
        <circle cx="12" cy="12" r="7" fill="var(--green)"/>
      </symbol>
      <symbol id="rate-half" viewBox="0 0 24 24">
        <circle cx="12" cy="12" r="9" fill="none" stroke="var(--yellow)" stroke-width="2.4" stroke-dasharray="28 29" transform="rotate(95 12 12)"/>
        <circle cx="13" cy="12" r="6.5" fill="var(--yellow)"/>
      </symbol>
      <symbol id="rate-low" viewBox="0 0 24 24">
        <circle cx="12" cy="12" r="9" fill="none" stroke="var(--orange)" stroke-width="2.4" stroke-dasharray="14 43" transform="rotate(180 12 12)"/>
        <circle cx="13" cy="13" r="6.5" fill="var(--orange)"/>
      </symbol>
      <symbol id="rate-none" viewBox="0 0 24 24">
        <circle cx="12" cy="12" r="6.5" fill="var(--dot-red)"/>
      </symbol>
    </defs>
  </svg>

  <table class="compare">
    <colgroup>
      <col class="c-feature"><col class="c-wax"><col class="c-ceramic"><col class="c-ppf">
    </colgroup>
    <thead>
      <tr><th class="feature">FEATURE</th><th>CAR WAX</th><th>CERAMIC COATING</th><th>PPF</th></tr>
    </thead>
    <tbody>
      <tr><td class="feature">Duration</td><td>2 - 4 Weeks</td><td>3 - 10 Years</td><td>7 - 10 Years</td></tr>
      <tr><td class="feature">Thickness</td><td>.5 - 1.5 microns</td><td>7 - 10 microns</td><td>200 - 250 microns</td></tr>
      <tr><td class="feature">Gloss Enhancement</td>
        <td><svg class="rating" aria-label="Excellent"><use href="#rate-full"/></svg></td>
        <td><svg class="rating" aria-label="Excellent"><use href="#rate-full"/></svg></td>
        <td><svg class="rating" aria-label="Excellent"><use href="#rate-full"/></svg></td></tr>
      <tr><td class="feature">Acid Rain Damage</td>
        <td><svg class="rating" aria-label="Fair"><use href="#rate-half"/></svg></td>
        <td><svg class="rating" aria-label="Excellent"><use href="#rate-full"/></svg></td>
        <td><svg class="rating" aria-label="Excellent"><use href="#rate-full"/></svg></td></tr>
      <tr><td class="feature">Corrosion Prevention</td>
        <td><svg class="rating" aria-label="Fair"><use href="#rate-half"/></svg></td>
        <td><svg class="rating" aria-label="Excellent"><use href="#rate-full"/></svg></td>
        <td><svg class="rating" aria-label="Excellent"><use href="#rate-full"/></svg></td></tr>
      <tr><td class="feature">UV/Oxidation Protection</td>
        <td><svg class="rating" aria-label="Fair"><use href="#rate-half"/></svg></td>
        <td><svg class="rating" aria-label="Excellent"><use href="#rate-full"/></svg></td>
        <td><svg class="rating" aria-label="Excellent"><use href="#rate-full"/></svg></td></tr>
      <tr><td class="feature">Hard Water Damage</td>
        <td><svg class="rating" aria-label="Low"><use href="#rate-low"/></svg></td>
        <td><svg class="rating" aria-label="Very good"><use href="#rate-most"/></svg></td>
        <td><svg class="rating" aria-label="Excellent"><use href="#rate-full"/></svg></td></tr>
      <tr><td class="feature">Insect Splatter Damage</td>
        <td><svg class="rating" aria-label="Low"><use href="#rate-low"/></svg></td>
        <td><svg class="rating" aria-label="Very good"><use href="#rate-most"/></svg></td>
        <td><svg class="rating" aria-label="Excellent"><use href="#rate-full"/></svg></td></tr>
      <tr><td class="feature">Chip Protection</td>
        <td><svg class="rating" aria-label="None"><use href="#rate-none"/></svg></td>
        <td><svg class="rating" aria-label="Low"><use href="#rate-low"/></svg></td>
        <td><svg class="rating" aria-label="Excellent"><use href="#rate-full"/></svg></td></tr>
      <tr><td class="feature">Scratch Protection</td>
        <td><svg class="rating" aria-label="None"><use href="#rate-none"/></svg></td>
        <td><svg class="rating" aria-label="Low"><use href="#rate-low"/></svg></td>
        <td><svg class="rating" aria-label="Excellent"><use href="#rate-full"/></svg></td></tr>
      <tr><td class="feature">Swirl Protection</td>
        <td><svg class="rating" aria-label="None"><use href="#rate-none"/></svg></td>
        <td><svg class="rating" aria-label="None"><use href="#rate-none"/></svg></td>
        <td><svg class="rating" aria-label="Excellent"><use href="#rate-full"/></svg></td></tr>
      <tr><td class="feature">Application Complexity</td><td>Low</td><td>Medium</td><td>High</td></tr>
    </tbody>
  </table>

</div>
</body>
</html>
```